Whole body Cryotherapy Tri fold Brochure

I am looking to do a tri fold brochure for a whole body cryotherapy business called Fernvale Cryotherapy.I do not have imagery but i would like to try to utilize images to support the benefits of Whole body cryotherapy. I will provide the content needed for the different sides. We would like to see blues and whatever would flow with the design. Also the machine that i will be using is called a PELOM and i would like to add that to the side flap of the brochure. I would really like this to be a modern unique twist since this type of treatment is fairly new to the United states.

Target Market(s)

women, men, children, athletes, health , modern medicine , alternative medicine

Industry/Entity Type

Alternative Medicine

Font styles to use
Sans Serif

Requirements
Must have
• Modern design with bold features, big colorful pictures.
Nice to have
• Font styles can be changed as well. Br

```html
<!DOCTYPE html>
<html lang="en">
<head>
<meta charset="utf-8">
<title>Fernvale Cryotherapy – Tri-fold Brochure</title>
<link href="https://fonts.googleapis.com/css2?family=Montserrat:wght@600;700;800&family=Open+Sans:wght@400;600&display=swap" rel="stylesheet">
<style>
:root{
  --blue:#1a73c9;
  --blue-dark:#0b3f80;
  --blue-light:#4db3f2;
  --ice:#e6f3fc;
  --ink:#333d47;
  --muted:#6b7682;
  --page:#ffffff;
  --photo-green-a:#7fae4a;
  --photo-green-b:#3f6e2a;
  --photo-sky-a:#bfe0f5;
  --photo-sky-b:#6e9fbf;
  --photo-skin-a:#e8c9ae;
  --photo-skin-b:#b98c6e;
}
*{box-sizing:border-box;margin:0;padding:0}
html,body{width:878px;height:1200px;overflow:hidden;background:var(--page)}
body{font-family:"Open Sans",Arial,sans-serif;color:var(--ink);position:relative}
.spread{position:absolute;left:20px;width:838px;height:570px;background:#fff;box-shadow:0 2px 8px rgba(0,0,0,.25);overflow:hidden;display:flex}
.spread.outside{top:18px}
.spread.inside{top:612px}
.panel{position:relative;width:279.33px;height:100%;overflow:hidden}
.panel + .panel{border-left:1px solid #e3e8ee}
.photo{position:absolute}
.swoosh{position:absolute;left:0;width:100%}
h2{font-family:"Montserrat",Arial,sans-serif;font-weight:800;color:var(--blue-dark);line-height:1.1}
h3{font-family:"Montserrat",Arial,sans-serif;font-weight:700;color:var(--blue);font-size:9px;line-height:1.3;margin:8px 0 3px}
p{font-size:7.6px;line-height:1.45;margin-bottom:5px}
.copy{position:absolute;left:20px;right:18px}
ul.benefits{list-style:none;font-size:7.6px;line-height:1.5}
ul.benefits li{padding-left:10px;position:relative}
ul.benefits li::before{content:"";position:absolute;left:0;top:4px;width:5px;height:5px;background:var(--blue);border-radius:50%}
.what-heading{font-size:19px}
.what-heading span{color:var(--blue)}
.contact{position:absolute;left:22px;top:292px;right:18px}
.contact-row{display:flex;align-items:center;gap:8px;font-size:9px;margin-bottom:9px;color:var(--ink)}
.contact-row svg{flex:none}
.contact-title{font-family:"Montserrat",Arial,sans-serif;font-weight:700;font-size:11px;color:var(--blue-dark);margin-bottom:10px;letter-spacing:.5px}
.badges{position:absolute;left:18px;right:18px;top:430px;display:grid;grid-template-columns:repeat(4,1fr);gap:8px}
.badge{height:18px;border-radius:3px;background:#c9d4de}
.badge.alt{background:#9fb3c6}
.badge.dark{background:#5d7288}
.brand{position:absolute;top:34px;left:0;right:0;display:flex;align-items:center;justify-content:center;gap:8px}
.brand-dot{width:26px;height:26px;border-radius:50%;background:var(--blue)}
.brand-name{font-family:"Montserrat",Arial,sans-serif;font-weight:800;font-size:16px;color:var(--blue-dark);line-height:1.05;letter-spacing:.5px}
.tagline-band{position:absolute;left:0;right:0;bottom:0;height:150px;background:var(--blue);display:flex;align-items:flex-end;padding:0 22px 34px}
.tagline{font-family:"Montserrat",Arial,sans-serif;font-weight:800;font-size:25px;color:#fff;line-height:1.1;text-align:right;width:100%}
.section-heading{font-size:13px;margin-bottom:6px}
.beauty-band{position:absolute;top:0;left:0;right:0;height:58px;background:var(--blue);display:flex;align-items:center;padding-left:22px}
.beauty-band h2{color:#fff;font-size:13px}
</style>
</head>
<body>

<section class="spread outside">
  <article class="panel panel-intro">
    <div class="photo" role="img" aria-label="Photo of a fit woman in sportswear" style="left:0;top:0;width:150px;height:200px;background:linear-gradient(160deg,var(--ice),var(--photo-skin-a) 60%,var(--photo-skin-b))"></div>
    <svg class="swoosh" style="top:0;height:220px" viewBox="0 0 279 220" preserveAspectRatio="none">
      <path d="M150 0 H279 V170 Q200 200 120 215 Q60 222 0 210 V200 Q90 195 150 150 Z" fill="var(--blue-light)" opacity=".35"/>
      <path d="M279 120 V210 Q180 220 0 222 V210 Q140 205 279 120 Z" fill="var(--blue)"/>
    </svg>
    <div class="copy" style="top:236px">
      <h2 class="what-heading">WHAT IS<br><span>WHOLE BODY</span><br>CRYOTHERAPY?</h2>
      <p style="margin-top:10px">Whole Body Cryotherapy is a process of cooling the body for a short time with dry, chilled air. The session lasts up to three minutes and helps the body begin its own natural recovery response.</p>
      <p>During a session the skin surface cools quickly while the core stays warm. Blood moves toward vital organs, then returns rich in oxygen and nutrients as the body warms again.</p>
      <p>Clients leave feeling refreshed, alert and energized. Many return for regular sessions to support recovery, wellness, beauty and an active lifestyle at any age.</p>
    </div>
  </article>

  <article class="panel panel-contact">
    <div class="photo" role="img" aria-label="Photo of a cyclist riding outdoors" style="left:0;top:0;width:100%;height:260px;background:linear-gradient(170deg,var(--photo-sky-a),var(--photo-sky-b) 55%,var(--photo-green-b))"></div>
    <svg class="swoosh" style="top:210px;height:60px" viewBox="0 0 279 60" preserveAspectRatio="none">
      <path d="M0 30 Q140 0 279 20 V60 H0 Z" fill="#fff"/>
      <path d="M0 30 Q140 0 279 20 V28 Q140 10 0 38 Z" fill="var(--blue)"/>
    </svg>
    <div class="contact">
      <div class="contact-title">CONTACT US</div>
      <div class="contact-row">
        <svg width="14" height="14" viewBox="0 0 24 24"><circle cx="12" cy="12" r="12" fill="var(--blue)"/><path d="M8 6l2 3-1 1.5c.8 1.7 2 2.9 3.5 3.5L14 13l3 2-1 2.5c-4.5-.5-8-4-8.5-8.5Z" fill="#fff"/></svg>
        (555) 014-2290
      </div>
      <div class="contact-row">
        <svg width="14" height="14" viewBox="0 0 24 24"><circle cx="12" cy="12" r="12" fill="var(--blue)"/><rect x="6" y="8" width="12" height="8" fill="#fff"/><path d="M6 8l6 5 6-5" stroke="var(--blue)" fill="none"/></svg>
        hello@fernvalecryo.com
      </div>
      <div class="contact-row">
        <svg width="14" height="14" viewBox="0 0 24 24"><circle cx="12" cy="12" r="12" fill="var(--blue)"/><path d="M12 5a4 4 0 0 1 4 4c0 3-4 8-4 8s-4-5-4-8a4 4 0 0 1 4-4Z" fill="#fff"/><circle cx="12" cy="9" r="1.4" fill="var(--blue)"/></svg>
        1420 Linden Avenue, Fernvale, NV 89999
      </div>
      <div class="contact-row">
        <svg width="14" height="14" viewBox="0 0 24 24"><circle cx="12" cy="12" r="12" fill="var(--blue)"/><circle cx="12" cy="12" r="5.5" stroke="#fff" fill="none" stroke-width="1.5"/><path d="M6.5 12h11M12 6.5v11" stroke="#fff" stroke-width="1.2"/></svg>
        www.fernvalecryo.com
      </div>
    </div>
    <div class="badges">
      <div class="badge"></div><div class="badge alt"></div><div class="badge dark"></div><div class="badge"></div>
      <div class="badge alt"></div><div class="badge"></div><div class="badge dark"></div><div class="badge alt"></div>
    </div>
  </article>

  <article class="panel panel-cover">
    <div class="brand">
      <span class="brand-dot"></span>
      <span class="brand-name">FERNVALE<br>CRYOTHERAPY</span>
    </div>
    <div class="photo" role="img" aria-label="Photo of a family cycling together in a park" style="left:0;top:110px;width:100%;height:320px;background:linear-gradient(175deg,var(--photo-green-a),var(--photo-green-b))"></div>
    <svg class="swoosh" style="top:100px;height:40px" viewBox="0 0 279 40" preserveAspectRatio="none">
      <path d="M0 0 H279 V10 Q140 40 0 20 Z" fill="#fff"/>
    </svg>
    <div class="tagline-band">
      <div class="tagline">FOR A BETTER<br>HEALTHIER YOU</div>
    </div>
    <svg class="swoosh" style="top:400px;height:40px" viewBox="0 0 279 40" preserveAspectRatio="none">
      <path d="M0 40 Q120 0 279 12 V40 Z" fill="var(--blue)"/>
      <path d="M0 34 Q120 -4 279 6 V10 Q120 4 0 40 Z" fill="var(--blue-light)"/>
    </svg>
  </article>
</section>

<section class="spread inside">
  <article class="panel panel-wellness">
    <div class="photo" role="img" aria-label="Photo of bare feet walking on fresh grass" style="left:0;top:0;width:180px;height:180px;background:linear-gradient(150deg,var(--photo-green-a),var(--photo-green-b))"></div>
    <svg class="swoosh" style="top:0;height:200px" viewBox="0 0 279 200" preserveAspectRatio="none">
      <path d="M180 0 H279 V200 H0 V185 Q110 170 180 0 Z" fill="#fff"/>
      <path d="M170 0 Q150 140 0 175 V190 Q160 160 190 0 Z" fill="var(--blue)"/>
      <path d="M200 0 Q190 110 279 150 V165 Q170 130 185 0 Z" fill="var(--blue-light)" opacity=".5"/>
    </svg>
    <div class="copy" style="top:200px">
      <h2 class="section-heading">HEALTH AND WELLNESS</h2>
      <p>Whole Body Cryotherapy can help ease a range of everyday conditions. Regular sessions may support joint comfort, reduce stiffness, lift mood and improve sleep. Many clients use it alongside their usual care to feel their best and stay active.</p>
      <h3>ADDITIONAL BENEFITS FOR HEALTH AND WELLNESS INCLUDE:</h3>
      <ul class="benefits">
        <li>Eases joint and muscle discomfort</li>
        <li>Supports a calm, balanced mood</li>
        <li>Promotes deeper, restful sleep</li>
        <li>Boosts energy and alertness</li>
        <li>Helps the body manage stress</li>
        <li>Supports a strong immune system</li>
        <li>Improves overall sense of wellbeing</li>
      </ul>
    </div>
  </article>

  <article class="panel panel-recovery">
    <svg class="swoosh" style="top:0;height:60px" viewBox="0 0 279 60" preserveAspectRatio="none">
      <path d="M0 0 H279 V20 Q150 60 0 40 Z" fill="var(--blue)"/>
    </svg>
    <div class="photo" role="img" aria-label="Photo of an athlete stretching after training" style="left:30px;top:60px;width:230px;height:150px;border-radius:4px;background:linear-gradient(160deg,var(--photo-sky-a),var(--photo-green-a) 60%,var(--photo-green-b))"></div>
    <div class="copy" style="top:226px">
      <h2 class="section-heading">RECOVERY AND PERFORMANCE</h2>
      <p>Professional teams and everyday athletes rely on cold therapy to recover faster between sessions. A short visit can reduce soreness and swelling after hard training, so you return ready to perform. It is a simple, drug-free way to support your goals and protect your body through every season.</p>
      <h3>ADDITIONAL BENEFITS OF WHOLE BODY CRYOTHERAPY FOR ATHLETES AND PERFORMANCE INCLUDE:</h3>
      <ul class="benefits">
        <li>Faster muscle recovery</li>
        <li>Less soreness after exercise</li>
        <li>Reduced swelling and tension</li>
        <li>More flexibility and range</li>
        <li>Higher energy levels</li>
        <li>Sharper focus before events</li>
      </ul>
    </div>
  </article>

  <article class="panel panel-beauty">
    <div class="beauty-band"><h2>BEAUTY AND ANTI-AGING</h2></div>
    <div class="photo" role="img" aria-label="Photo of a woman with glowing skin" style="right:0;top:58px;width:110px;height:90px;background:linear-gradient(160deg,var(--photo-skin-a),var(--photo-skin-b))"></div>
    <div class="copy" style="top:150px">
      <h3 style="margin-top:0">INCREASED METABOLISM AND WEIGHT LOSS</h3>
      <p>As the body warms after a session, it burns extra calories to restore its natural temperature. Paired with healthy habits, regular visits can support weight goals and a more active metabolism.</p>
      <h3>ANTI-AGING</h3>
      <p>Cold exposure encourages fresh circulation to the skin and supports natural collagen. Clients often notice a brighter, firmer and more even complexion over time.</p>
      <h3>ADDITIONAL BENEFITS</h3>
      <ul class="benefits">
        <li>Tighter, smoother looking skin</li>
        <li>Healthy, radiant glow</li>
        <li>Reduced puffiness</li>
        <li>Improved skin tone</li>
        <li>Renewed confidence</li>
      </ul>
    </div>
    <div class="photo" role="img" aria-label="Photo of a woman jumping for joy outdoors" style="left:0;top:470px;width:100%;height:100px;background:linear-gradient(170deg,var(--photo-sky-a),var(--photo-sky-b))"></div>
    <svg class="swoosh" style="top:462px;height:30px" viewBox="0 0 279 30" preserveAspectRatio="none">
      <path d="M0 0 H279 V8 Q140 30 0 12 Z" fill="#fff"/>
      <path d="M0 12 Q140 30 279 8 V14 Q140 34 0 18 Z" fill="var(--blue)"/>
    </svg>
  </article>
</section>

</body>
</html>
```